VORIKA FLYER 2019

Hi, We need an A4 flyer design for our cleaning company, focusing on dry carpet cleaning I attached our catalogue to give some idea. In addition, our websites can provide more information. Our Services:-General Cleaning Carry out heavy cleansing tasks and special projects. Clean, stock and supply designated facility areas (dusting, sweeping, vacuuming, mopping, cleaning ceiling vents, restroom cleaning etc).Using electrically powered scrubbing and polishing machines to burnish, scrub, polish and spray clean floors. Window Cleaning Regular, Reliable Window Cleaning. Hard To Reach Windows. Single 7 Multi-Storey. Frames and Glass Cleaned. Floor Cleaning Marble Cleaning & Polishing. Tile & Grout Cleaning. Hardwood Floors Services. Vinyl Floors. The PLUME Dry Extraction Carpet Cleaning System uses environmentally preferred, Clear Leaf Certified cleaning products that deep cleans your carpets and textured hard floors quickly and easily.

Target Market(s)

Residential and Commercial.
Offices, Hospitals, Restaurants, Etc.

Industry/Entity Type

Cleaning Service

Font styles to use
Serif
Sans Serif

Colors
33a6d7
0592cd
85cae6
85acd3
3277b5
296eb1

Requirements
Must have
• CREATIVE AND MINIMAL
Nice to have
• Engaging Pics and Texts

```html
<!DOCTYPE html>
<html lang="en">
<head>
<meta charset="utf-8">
<title>Vorika Cleaning &amp; Maintenance – Dry Carpet Cleaning Flyer</title>
<link rel="stylesheet" href="https://fonts.googleapis.com/css2?family=Bebas+Neue&family=Roboto:wght@400;500&family=Montserrat:wght@500;700;800&display=swap">
<style>
  :root{
    --page-bg:#d6d6d6;
    --paper:#ffffff;
    --navy:#2b2a78;
    --navy-text:#26246e;
    --carpet:#3a3489;
    --box-top:#2f2cae;
    --box-bottom:#1c1568;
    --footer-grey:#6b6b6d;
    --body-text:#333333;
    --photo-light:#e9dccb;
    --photo-mid:#9aa2b4;
    --photo-dark:#5d6a86;
    --white:#ffffff;
  }
  *{box-sizing:border-box;margin:0;padding:0}
  html,body{width:703px;height:1200px;overflow:hidden;background:var(--page-bg)}
  .flyer{position:absolute;left:0;top:103px;width:703px;height:994px;background:var(--paper);overflow:hidden;box-shadow:6px 6px 10px rgba(0,0,0,.35)}
  .hero-photo{position:absolute;left:0;top:40px;width:703px;height:500px;background:linear-gradient(100deg,var(--photo-light) 0%,#d9cdbd 30%,var(--photo-mid) 60%,var(--photo-dark) 100%)}
  .shape-layer{position:absolute;left:0;top:0;width:703px;height:994px}
  .brand{position:absolute;left:0;top:28px;width:703px;text-align:center;color:var(--navy);font-family:'Montserrat',sans-serif;font-weight:700;font-size:17px;line-height:1.25;letter-spacing:1px}
  .headline{position:absolute;left:0;width:730px;text-align:center;color:var(--white)}
  .headline-title{top:452px;font-family:'Bebas Neue',sans-serif;font-size:62px;line-height:1;letter-spacing:.5px}
  .headline-tag{top:506px;font-family:'Roboto',sans-serif;font-size:20px;line-height:1}
  .hex{position:absolute;width:172px;height:150px;clip-path:polygon(25% 0,75% 0,100% 50%,75% 100%,25% 100%,0 50%)}
  .hex-machine{left:324px;top:548px;background:linear-gradient(160deg,#e4ded6,#8f96a3 55%,#c9bfb2)}
  .hex-worker{left:492px;top:516px;background:linear-gradient(160deg,#d8cbb8,#3d5fb0 55%,#b49a86)}
  .services{position:absolute;left:43px;top:555px;width:300px;font-family:'Roboto',sans-serif;color:var(--body-text)}
  .services-title{font-family:'Montserrat',sans-serif;font-weight:800;font-size:19px;color:var(--navy-text);line-height:1.1}
  .services-title::after{content:"";display:block;width:38px;height:2px;background:var(--navy-text);margin-top:2px}
  .services-intro{font-size:10px;line-height:1.2;margin-top:12px;width:260px}
  .service-list{list-style:none;margin-top:13px}
  .service-item{position:relative;padding-left:28px;max-width:278px;font-size:9.6px;line-height:1.22;margin-bottom:9px;font-weight:400}
  .service-item svg{position:absolute;left:2px;top:0;width:13px;height:13px}
  .facility-box{position:absolute;left:407px;top:694px;width:258px;height:288px;border:3px solid var(--white);border-radius:8px 8px 0 0;background:linear-gradient(180deg,var(--box-top),var(--box-bottom));padding:14px 0 0 27px;color:var(--white)}
  .facility-title{font-family:'Montserrat',sans-serif;font-weight:700;font-size:13.4px;line-height:1.2}
  .facility-list{list-style:none;margin-top:22px}
  .facility-item{display:flex;align-items:center;gap:18px;height:29.2px;font-family:'Roboto',sans-serif;font-weight:500;font-size:12.5px}
  .facility-icon{width:24px;height:24px;flex:none}
  .contact{position:absolute;left:43px;top:928px;color:var(--white)}
  .contact-call{font-family:'Montserrat',sans-serif;font-size:11.5px;font-weight:500;letter-spacing:.5px;display:flex;align-items:baseline;gap:8px}
  .contact-phone{font-size:22px;font-weight:500;letter-spacing:.5px}
  .contact-links{display:flex;gap:16px;margin-top:6px;font-family:'Montserrat',sans-serif;font-size:11.5px;font-weight:500}
  .contact-link{display:flex;align-items:center;gap:6px}
  .contact-link svg{width:13px;height:13px}
</style>
</head>
<body>
<main class="flyer">
  <div class="hero-photo" role="img" aria-label="Photo of a woman kneeling and vacuuming a carpet beside a bright window and sofa"></div>

  <svg class="shape-layer" viewBox="0 0 703 994" aria-hidden="true">
    <path class="header-curve" d="M0,0 H703 V57 Q380,122 0,62 Z" fill="#ffffff"/>
    <path class="carpet-band" d="M0,540 V428 Q260,388 703,392 V540 Z" fill="#3a3489"/>
    <path class="footer-band" d="M0,918 H382 Q400,918 408,934 L432,994 H0 Z" fill="#6b6b6d"/>
  </svg>

  <header class="brand">VORIKA CLEANING<br>&amp; MAINTENANCE</header>

  <h1 class="headline headline-title">DRY CARPET CLEANING</h1>
  <p class="headline headline-tag">Clean Floors, Better For Business</p>

  <div class="hex hex-machine" role="img" aria-label="Photo of an electric floor scrubbing and polishing machine"></div>
  <div class="hex hex-worker" role="img" aria-label="Photo of a cleaner in blue overalls operating a floor machine"></div>

  <section class="services">
    <h2 class="services-title">OUR SERVICES</h2>
    <p class="services-intro">General Cleaning Carry out heavy cleansing tasks and special projects</p>
    <ul class="service-list">
      <li class="service-item"><svg viewBox="0 0 14 14"><circle cx="7" cy="7" r="5.8" fill="none" stroke="#2b2a78" stroke-width="1.3"/><path d="M4.2,7.2 L6.3,9.2 L12.5,2.8" fill="none" stroke="#2b2a78" stroke-width="1.4"/></svg>Using electrically powered scrubbing and polishing machines to burnish</li>
      <li class="service-item"><svg viewBox="0 0 14 14"><circle cx="7" cy="7" r="5.8" fill="none" stroke="#2b2a78" stroke-width="1.3"/><path d="M4.2,7.2 L6.3,9.2 L12.5,2.8" fill="none" stroke="#2b2a78" stroke-width="1.4"/></svg>Scrub, polish and spray clean floors</li>
      <li class="service-item"><svg viewBox="0 0 14 14"><circle cx="7" cy="7" r="5.8" fill="none" stroke="#2b2a78" stroke-width="1.3"/><path d="M4.2,7.2 L6.3,9.2 L12.5,2.8" fill="none" stroke="#2b2a78" stroke-width="1.4"/></svg>Window Cleaning Regular, Reliable Window<br>Cleaning</li>
      <li class="service-item"><svg viewBox="0 0 14 14"><circle cx="7" cy="7" r="5.8" fill="none" stroke="#2b2a78" stroke-width="1.3"/><path d="M4.2,7.2 L6.3,9.2 L12.5,2.8" fill="none" stroke="#2b2a78" stroke-width="1.4"/></svg>Hard To Reach Windows. Single 7 Multi-Storey.</li>
      <li class="service-item"><svg viewBox="0 0 14 14"><circle cx="7" cy="7" r="5.8" fill="none" stroke="#2b2a78" stroke-width="1.3"/><path d="M4.2,7.2 L6.3,9.2 L12.5,2.8" fill="none" stroke="#2b2a78" stroke-width="1.4"/></svg>Frames and Glass Cleaned.</li>
      <li class="service-item"><svg viewBox="0 0 14 14"><circle cx="7" cy="7" r="5.8" fill="none" stroke="#2b2a78" stroke-width="1.3"/><path d="M4.2,7.2 L6.3,9.2 L12.5,2.8" fill="none" stroke="#2b2a78" stroke-width="1.4"/></svg>Floor Cleaning Marble Cleaning &amp; Polishing.</li>
      <li class="service-item"><svg viewBox="0 0 14 14"><circle cx="7" cy="7" r="5.8" fill="none" stroke="#2b2a78" stroke-width="1.3"/><path d="M4.2,7.2 L6.3,9.2 L12.5,2.8" fill="none" stroke="#2b2a78" stroke-width="1.4"/></svg>Tile &amp; Grout Cleaning.</li>
      <li class="service-item"><svg viewBox="0 0 14 14"><circle cx="7" cy="7" r="5.8" fill="none" stroke="#2b2a78" stroke-width="1.3"/><path d="M4.2,7.2 L6.3,9.2 L12.5,2.8" fill="none" stroke="#2b2a78" stroke-width="1.4"/></svg>Hardwood Floors Services.</li>
      <li class="service-item"><svg viewBox="0 0 14 14"><circle cx="7" cy="7" r="5.8" fill="none" stroke="#2b2a78" stroke-width="1.3"/><path d="M4.2,7.2 L6.3,9.2 L12.5,2.8" fill="none" stroke="#2b2a78" stroke-width="1.4"/></svg>Vinyl Floors.</li>
      <li class="service-item"><svg viewBox="0 0 14 14"><circle cx="7" cy="7" r="5.8" fill="none" stroke="#2b2a78" stroke-width="1.3"/><path d="M4.2,7.2 L6.3,9.2 L12.5,2.8" fill="none" stroke="#2b2a78" stroke-width="1.4"/></svg>The PLUME Dry Extraction Carpet Cleaning System uses environmentally preferred, Clear Leaf Certified cleaning products that deep cleans your carpets and textured hard floors quickly and easily.</li>
    </ul>
  </section>

  <aside class="facility-box">
    <h3 class="facility-title">CLEAN, STOCK AND SUPPLY<br>DESIGNATED FACILITY</h3>
    <ul class="facility-list">
      <li class="facility-item"><svg class="facility-icon" viewBox="0 0 24 24"><circle cx="12" cy="12" r="12" fill="#fff"/><circle cx="11" cy="6.5" r="1.8" fill="#2b2a78"/><path d="M9,9 H13 V18 H9 Z M14,12 H17 V18 H14 Z" fill="#2b2a78"/></svg>Dusting</li>
      <li class="facility-item"><svg class="facility-icon" viewBox="0 0 24 24"><circle cx="12" cy="12" r="12" fill="#fff"/><circle cx="11" cy="6" r="1.8" fill="#2b2a78"/><path d="M9,8.5 H13 L13.5,14 L12,19 H10 L10.5,14 Z" fill="#2b2a78"/><path d="M15,7 L16,17 M14,17 H18" stroke="#2b2a78" stroke-width="1.3"/></svg>Sweeping</li>
      <li class="facility-item"><svg class="facility-icon" viewBox="0 0 24 24"><circle cx="12" cy="12" r="12" fill="#fff"/><path d="M15,5 L10,17" stroke="#2b2a78" stroke-width="1.5"/><path d="M7,17 H13 V19 H7 Z" fill="#2b2a78"/><circle cx="16" cy="15" r="2.5" fill="#2b2a78"/></svg>Vacuuming</li>
      <li class="facility-item"><svg class="facility-icon" viewBox="0 0 24 24"><circle cx="12" cy="12" r="12" fill="#fff"/><path d="M9,5 L12,16" stroke="#2b2a78" stroke-width="1.5"/><path d="M8,16 H17 L16,19 H8 Z" fill="#2b2a78"/></svg>Mopping</li>
      <li class="facility-item"><svg class="facility-icon" viewBox="0 0 24 24"><circle cx="12" cy="12" r="12" fill="#fff"/><rect x="6" y="8" width="12" height="8" fill="none" stroke="#2b2a78" stroke-width="1.4"/><path d="M8,10.5 H16 M8,12 H16 M8,13.5 H16" stroke="#2b2a78" stroke-width="1"/></svg>Cleaning ceiling vents</li>
      <li class="facility-item"><svg class="facility-icon" viewBox="0 0 24 24"><circle cx="12" cy="12" r="12" fill="#fff"/><rect x="6" y="7" width="12" height="10" fill="none" stroke="#2b2a78" stroke-width="1.4"/><path d="M12,7 V17" stroke="#2b2a78" stroke-width="1.2"/><circle cx="9" cy="10" r="1" fill="#2b2a78"/><circle cx="15" cy="10" r="1" fill="#2b2a78"/><path d="M8,12 H10 V15 H8 Z M14,12 H16 V15 H14 Z" fill="#2b2a78"/></svg>Restroom cleaning</li>
    </ul>
  </aside>

  <footer class="contact">
    <p class="contact-call">CALL US NOW: <span class="contact-phone">012-555-0147</span></p>
    <div class="contact-links">
      <span class="contact-link"><svg viewBox="0 0 14 14"><circle cx="7" cy="7" r="6" fill="none" stroke="#fff" stroke-width="1.3"/><path d="M1,7 H13 M7,1 C3.5,4 3.5,10 7,13 C10.5,10 10.5,4 7,1" fill="none" stroke="#fff" stroke-width="1"/></svg>www.vorikaclean.com</span>
      <span class="contact-link"><svg viewBox="0 0 14 14"><rect x="1" y="3" width="12" height="8" fill="none" stroke="#fff" stroke-width="1.3"/><path d="M1,3 L7,8 L13,3" fill="none" stroke="#fff" stroke-width="1.2"/></svg>hello@vorikaclean.com</span>
    </div>
  </footer>
</main>
</body>
</html>
```